Accommodation business card design

We need a business card designed for our long-term accommodation business based in Australia. The business card must match the style of the attached letterhead and logo. The same contact details that are on the letterhead will also go on the card except that the card must list the contact details in the following order:phone, email, home address, ABN.

The card will be printed on .76mm white pvc plastic (same as credit cards), printed both sides and will be silver foil stamped on at least one side (preferably 2 sides) The design template is attached, but please go to www.zt.com.au for more specs.

The only other addition the card will be my name: Malcolm Darby

```html
<!DOCTYPE html>
<html lang="en">
<head>
<meta charset="utf-8">
<title>Summit Lodging – Business Card</title>
<link rel="stylesheet" href="https://fonts.googleapis.com/css2?family=Oswald:wght@600&family=Open+Sans:wght@400&display=swap">
<style>
  :root {
    --page-bg: #ecebea;
    --card-white: #ffffff;
    --card-shade: #e4e4e6;
    --brand-red: #9c4b45;
    --brand-maroon: #7e1f45;
    --brand-magenta: #b02a6c;
    --brand-wine: #64132f;
    --band-clay: #a85a50;
    --text-grey: #555559;
  }
  html, body {
    margin: 0;
    padding: 0;
    width: 1200px;
    height: 1132px;
    overflow: hidden;
    background: var(--page-bg);
  }
  .canvas {
    position: relative;
    width: 1200px;
    height: 1132px;
  }
  .card {
    position: absolute;
    left: 255px;
    width: 700px;
    height: 435px;
    border-radius: 26px;
    overflow: hidden;
    background: radial-gradient(ellipse at 55% 35%, var(--card-white) 40%, var(--card-shade) 100%);
    box-shadow: 0 4px 14px rgba(0,0,0,0.18);
  }
  .card--front { top: 96px; }
  .card--back  { top: 556px; }
  .card__swoosh {
    position: absolute;
    inset: 0;
    width: 700px;
    height: 435px;
  }
  .brand {
    position: absolute;
    display: flex;
    align-items: center;
  }
  .brand__mark {
    background: var(--brand-maroon);
    border-radius: 14px;
    flex: none;
  }
  .brand__name {
    font-family: "Oswald", "Arial Narrow", sans-serif;
    font-weight: 600;
    color: var(--brand-red);
    text-transform: uppercase;
    line-height: 1.02;
    letter-spacing: 1px;
  }
  .card--front .brand { left: 143px; top: 137px; }
  .card--front .brand__mark { width: 127px; height: 127px; margin-right: 22px; }
  .card--front .brand__name { font-size: 54px; }
  .card--back .brand { left: 236px; top: 41px; }
  .card--back .brand__mark { width: 97px; height: 97px; margin-right: 16px; border-radius: 11px; }
  .card--back .brand__name { font-size: 41px; }
  .contact {
    position: absolute;
    left: 236px;
    top: 168px;
    margin: 0;
    padding: 0;
    list-style: none;
    font-family: "Open Sans", Arial, sans-serif;
    font-size: 22px;
    color: var(--text-grey);
    line-height: 33.5px;
  }
  .contact__item {
    display: flex;
    align-items: flex-start;
  }
  .contact__icon {
    flex: none;
    width: 22px;
    height: 22px;
    margin: 6px 12px 0 0;
  }
  .contact__item--plain { padding-left: 34px; }
  .contact__item--abn { padding-left: 34px; }
  .contact__label { color: var(--brand-maroon); margin-right: 6px; }
</style>
</head>
<body>
<main class="canvas">

  <section class="card card--front" aria-label="Card front">
    <svg class="card__swoosh" viewBox="0 0 700 435" aria-hidden="true">
      <path d="M155 350 C 330 340, 560 320, 700 262 L 700 300 C 560 340, 330 352, 155 350 Z" fill="var(--band-clay)"/>
      <path d="M155 350 C 340 354, 560 338, 700 292 L 700 383 C 560 395, 340 372, 155 350 Z" fill="var(--brand-maroon)"/>
    </svg>
    <div class="brand">
      <div class="brand__mark"></div>
      <div class="brand__name">Summit<br>Lodging</div>
    </div>
  </section>

  <section class="card card--back" aria-label="Card back">
    <svg class="card__swoosh" viewBox="0 0 700 435" aria-hidden="true">
      <defs>
        <linearGradient id="backBand" x1="0" y1="0" x2="1" y2="0.3">
          <stop offset="0" stop-color="var(--brand-magenta)"/>
          <stop offset="1" stop-color="var(--brand-wine)"/>
        </linearGradient>
      </defs>
      <path d="M0 190 C 40 300, 180 380, 420 395 C 560 402, 650 395, 700 385 L 700 402 C 600 412, 420 412, 280 395 C 130 372, 30 300, 0 225 Z" fill="var(--band-clay)"/>
      <path d="M0 225 C 40 320, 180 395, 420 408 C 560 414, 650 410, 700 402 L 700 435 L 0 435 Z" fill="url(#backBand)"/>
    </svg>
    <div class="brand">
      <div class="brand__mark"></div>
      <div class="brand__name">Summit<br>Lodging</div>
    </div>
    <ul class="contact">
      <li class="contact__item">
        <svg class="contact__icon" viewBox="0 0 22 22" aria-hidden="true">
          <circle cx="11" cy="11" r="11" fill="var(--brand-maroon)"/>
          <path d="M7.5 5.5 l2 2.5 -1.2 1.4 c0.8 1.8 2 3 3.8 3.8 l1.4-1.2 2.5 2 -1.2 2 c-4.5-0.4-8.4-4.3-8.8-8.8z" fill="#fff"/>
        </svg>
        <span>0400 318 562</span>
      </li>
      <li class="contact__item">
        <svg class="contact__icon" viewBox="0 0 22 22" aria-hidden="true">
          <circle cx="11" cy="11" r="11" fill="var(--brand-maroon)"/>
          <rect x="5.5" y="7" width="11" height="8" fill="#fff"/>
          <path d="M5.5 7 L11 11.5 L16.5 7" fill="none" stroke="var(--brand-maroon)" stroke-width="1.2"/>
        </svg>
        <span>malcolm.darby@zt.com.au</span>
      </li>
      <li class="contact__item">
        <svg class="contact__icon" viewBox="0 0 22 22" aria-hidden="true">
          <circle cx="11" cy="11" r="11" fill="var(--brand-maroon)"/>
          <path d="M11 5 L17 10.5 L15.5 10.5 L15.5 16 L6.5 16 L6.5 10.5 L5 10.5 Z" fill="#fff"/>
          <rect x="9.6" y="12" width="2.8" height="4" fill="var(--brand-maroon)"/>
        </svg>
        <span>PO Box 1180, Bayside Mail Centre</span>
      </li>
      <li class="contact__item contact__item--plain">QLD 4700</li>
      <li class="contact__item contact__item--abn"><span class="contact__label">ABN</span>12 345 678 901</li>
    </ul>
  </section>

</main>
</body>
</html>
```